Themed Business Cards

1. Document should be in a word, and word template (5 across x 2). See attached documents.
2. Font is Arial
3. Include REIMAGINE YOUR FUTURE on the back side of the card
4. Include placement for Brightpath Logo and the Partner Network Logo on the front side of the card.

Target Market(s)

The business cards are used to promote the association

Requirements
Must have
• Correct Colors
Use Arial font
Use of Brightpath Logo and Partner Network Logos or Theme Logo only
Be editable for members to customize
Template for business cards

TEAL:
C67, M10, Y35, K12
R69, G158, B156

BLUE:
C100, M4, Y0, K28
R0, G130, B181

RED:
C10, M100, Y100, K5
R207, G31, B37

ORANGE:
C0, M65, Y98, K10
R221, G110, B32

```html
<!DOCTYPE html>
<html lang="en">
<head>
<meta charset="utf-8">
<title>Themed Business Cards</title>
<link href="https://fonts.googleapis.com/css2?family=Arimo:wght@400;700&display=swap" rel="stylesheet">
<style>
  :root {
    --orange: #dd6e20;
    --orange-light: #ea7a2a;
    --red: #cf1f25;
    --teal: #459e9c;
    --blue: #0082b5;
    --white: #ffffff;
    --paper: #f4f4f4;
    --sheet-edge: #d6d6d6;
    --back-grey: #ececec;
  }
  * { box-sizing: border-box; margin: 0; padding: 0; }
  html, body { width: 811px; height: 1200px; overflow: hidden; }
  body {
    background: var(--paper);
    font-family: "Arimo", Arial, sans-serif;
    position: relative;
  }

  .card {
    position: relative;
    width: 108px;
    height: 170px;
    overflow: hidden;
    flex: none;
  }

  /* Front side */
  .card-front {
    background: linear-gradient(165deg, var(--orange-light) 0%, var(--orange) 40%, var(--red) 100%);
    color: var(--white);
  }
  .card-front .sheen {
    position: absolute; inset: 0;
    background: rgba(255,255,255,0.12);
    clip-path: polygon(0 52%, 100% 34%, 100% 62%, 0 80%);
  }
  .card-front .org-line {
    position: absolute; top: 11px; left: 4px; right: 4px;
    text-align: center; font-size: 4.4px; letter-spacing: 0.2px;
    white-space: nowrap;
  }
  .card-front .name {
    position: absolute; top: 33px; left: 10px;
    font-size: 10px; font-weight: 700; white-space: nowrap;
  }
  .card-front .title {
    position: absolute; top: 46px; left: 10px; font-size: 5px;
  }
  .card-front .rep-band {
    position: absolute; top: 57px; left: 8px; width: 70px; height: 11px;
    background: var(--white); display: flex; align-items: center;
  }
  .rep-band .rep-label {
    background: var(--red); color: var(--white);
    font-size: 5px; font-weight: 700; padding: 0 4px; height: 100%;
    display: flex; align-items: center;
  }
  .rep-band .rep-term { color: var(--orange); font-size: 5px; font-weight: 700; padding-left: 4px; }
  .card-front .contact {
    position: absolute; top: 93px; left: 9px; right: 6px;
    display: grid; grid-template-columns: 44px 1fr; gap: 3px 3px;
    font-size: 4px; font-weight: 700; white-space: nowrap;
  }
  .card-front .web {
    position: absolute; bottom: 10px; left: 0; right: 0;
    text-align: center; font-size: 4.4px;
  }

  /* Back side */
  .card-back { background: linear-gradient(90deg, var(--white) 0%, var(--back-grey) 100%); }
  .card-back svg { position: absolute; inset: 0; }
  .card-back .emblem {
    position: absolute; top: 60px; left: 29px; width: 50px; height: 50px;
    border-radius: 50%; border: 3px solid var(--orange);
    display: flex; align-items: center; justify-content: center;
    color: var(--orange); font-size: 7px; font-weight: 700;
  }
  .card-back .tagline {
    position: absolute; top: 116px; left: 0; right: 0; text-align: center;
    color: var(--orange); font-size: 4.4px; font-weight: 700; letter-spacing: 0.3px;
  }

  /* Layout */
  .preview {
    position: absolute; top: 18px; left: 0; right: 0;
    display: flex; justify-content: center; gap: 14px;
  }
  .sheet {
    position: absolute; left: 140px; width: 600px;
    background: var(--white); border: 1px solid var(--sheet-edge);
    padding: 14px 19px;
    display: grid; grid-template-columns: repeat(5, 108px); gap: 6px 5px;
  }
  .sheet-backs { top: 225px; }
  .sheet-fronts { top: 745px; }
</style>
</head>
<body>

<section class="preview">
  <div class="card card-front">
    <div class="sheen"></div>
    <div class="org-line">BRIGHTPATH · PARTNER NETWORK</div>
    <div class="name">Dana Whitfield</div>
    <div class="title">Member</div>
    <div class="rep-band"><span class="rep-label">REP</span><span class="rep-term">2013-2014</span></div>
    <div class="contact"><span>555.010.2040</span><span>dana@brightpath.org</span><span>12 Elm Street</span><span>Springfield, ST</span></div>
    <div class="web">www.brightpath.org</div>
  </div>
  <div class="card card-back">
    <svg viewBox="0 0 108 170" width="108" height="170" aria-hidden="true">
      <polygon points="0,0 108,0 108,18 0,48" fill="#dd6e20"/>
      <polygon points="0,152 108,122 108,170 0,170" fill="#dd6e20"/>
    </svg>
    <div class="emblem">Brightpath</div>
    <div class="tagline">REIMAGINE YOUR FUTURE</div>
  </div>
</section>

<section class="sheet sheet-backs">
  <div class="card card-back"><svg viewBox="0 0 108 170" width="108" height="170" aria-hidden="true"><polygon points="0,0 108,0 108,18 0,48" fill="#dd6e20"/><polygon points="0,152 108,122 108,170 0,170" fill="#dd6e20"/></svg><div class="emblem">Brightpath</div><div class="tagline">REIMAGINE YOUR FUTURE</div></div>
  <div class="card card-back"><svg viewBox="0 0 108 170" width="108" height="170" aria-hidden="true"><polygon points="0,0 108,0 108,18 0,48" fill="#dd6e20"/><polygon points="0,152 108,122 108,170 0,170" fill="#dd6e20"/></svg><div class="emblem">Brightpath</div><div class="tagline">REIMAGINE YOUR FUTURE</div></div>
  <div class="card card-back"><svg viewBox="0 0 108 170" width="108" height="170" aria-hidden="true"><polygon points="0,0 108,0 108,18 0,48" fill="#dd6e20"/><polygon points="0,152 108,122 108,170 0,170" fill="#dd6e20"/></svg><div class="emblem">Brightpath</div><div class="tagline">REIMAGINE YOUR FUTURE</div></div>
  <div class="card card-back"><svg viewBox="0 0 108 170" width="108" height="170" aria-hidden="true"><polygon points="0,0 108,0 108,18 0,48" fill="#dd6e20"/><polygon points="0,152 108,122 108,170 0,170" fill="#dd6e20"/></svg><div class="emblem">Brightpath</div><div class="tagline">REIMAGINE YOUR FUTURE</div></div>
  <div class="card card-back"><svg viewBox="0 0 108 170" width="108" height="170" aria-hidden="true"><polygon points="0,0 108,0 108,18 0,48" fill="#dd6e20"/><polygon points="0,152 108,122 108,170 0,170" fill="#dd6e20"/></svg><div class="emblem">Brightpath</div><div class="tagline">REIMAGINE YOUR FUTURE</div></div>
  <div class="card card-back"><svg viewBox="0 0 108 170" width="108" height="170" aria-hidden="true"><polygon points="0,0 108,0 108,18 0,48" fill="#dd6e20"/><polygon points="0,152 108,122 108,170 0,170" fill="#dd6e20"/></svg><div class="emblem">Brightpath</div><div class="tagline">REIMAGINE YOUR FUTURE</div></div>
  <div class="card card-back"><svg viewBox="0 0 108 170" width="108" height="170" aria-hidden="true"><polygon points="0,0 108,0 108,18 0,48" fill="#dd6e20"/><polygon points="0,152 108,122 108,170 0,170" fill="#dd6e20"/></svg><div class="emblem">Brightpath</div><div class="tagline">REIMAGINE YOUR FUTURE</div></div>
  <div class="card card-back"><svg viewBox="0 0 108 170" width="108" height="170" aria-hidden="true"><polygon points="0,0 108,0 108,18 0,48" fill="#dd6e20"/><polygon points="0,152 108,122 108,170 0,170" fill="#dd6e20"/></svg><div class="emblem">Brightpath</div><div class="tagline">REIMAGINE YOUR FUTURE</div></div>
  <div class="card card-back"><svg viewBox="0 0 108 170" width="108" height="170" aria-hidden="true"><polygon points="0,0 108,0 108,18 0,48" fill="#dd6e20"/><polygon points="0,152 108,122 108,170 0,170" fill="#dd6e20"/></svg><div class="emblem">Brightpath</div><div class="tagline">REIMAGINE YOUR FUTURE</div></div>
  <div class="card card-back"><svg viewBox="0 0 108 170" width="108" height="170" aria-hidden="true"><polygon points="0,0 108,0 108,18 0,48" fill="#dd6e20"/><polygon points="0,152 108,122 108,170 0,170" fill="#dd6e20"/></svg><div class="emblem">Brightpath</div><div class="tagline">REIMAGINE YOUR FUTURE</div></div>
</section>

<section class="sheet sheet-fronts">
  <div class="card card-front"><div class="sheen"></div><div class="org-line">BRIGHTPATH · PARTNER NETWORK</div><div class="name">Dana Whitfield</div><div class="title">Member</div><div class="rep-band"><span class="rep-label">REP</span><span class="rep-term">2013-2014</span></div><div class="contact"><span>555.010.2040</span><span>dana@brightpath.org</span><span>12 Elm Street</span><span>Springfield, ST</span></div><div class="web">www.brightpath.org</div></div>
  <div class="card card-front"><div class="sheen"></div><div class="org-line">BRIGHTPATH · PARTNER NETWORK</div><div class="name">Dana Whitfield</div><div class="title">Member</div><div class="rep-band"><span class="rep-label">REP</span><span class="rep-term">2013-2014</span></div><div class="contact"><span>555.010.2040</span><span>dana@brightpath.org</span><span>12 Elm Street</span><span>Springfield, ST</span></div><div class="web">www.brightpath.org</div></div>
  <div class="card card-front"><div class="sheen"></div><div class="org-line">BRIGHTPATH · PARTNER NETWORK</div><div class="name">Dana Whitfield</div><div class="title">Member</div><div class="rep-band"><span class="rep-label">REP</span><span class="rep-term">2013-2014</span></div><div class="contact"><span>555.010.2040</span><span>dana@brightpath.org</span><span>12 Elm Street</span><span>Springfield, ST</span></div><div class="web">www.brightpath.org</div></div>
  <div class="card card-front"><div class="sheen"></div><div class="org-line">BRIGHTPATH · PARTNER NETWORK</div><div class="name">Dana Whitfield</div><div class="title">Member</div><div class="rep-band"><span class="rep-label">REP</span><span class="rep-term">2013-2014</span></div><div class="contact"><span>555.010.2040</span><span>dana@brightpath.org</span><span>12 Elm Street</span><span>Springfield, ST</span></div><div class="web">www.brightpath.org</div></div>
  <div class="card card-front"><div class="sheen"></div><div class="org-line">BRIGHTPATH · PARTNER NETWORK</div><div class="name">Dana Whitfield</div><div class="title">Member</div><div class="rep-band"><span class="rep-label">REP</span><span class="rep-term">2013-2014</span></div><div class="contact"><span>555.010.2040</span><span>dana@brightpath.org</span><span>12 Elm Street</span><span>Springfield, ST</span></div><div class="web">www.brightpath.org</div></div>
  <div class="card card-front"><div class="sheen"></div><div class="org-line">BRIGHTPATH · PARTNER NETWORK</div><div class="name">Dana Whitfield</div><div class="title">Member</div><div class="rep-band"><span class="rep-label">REP</span><span class="rep-term">2013-2014</span></div><div class="contact"><span>555.010.2040</span><span>dana@brightpath.org</span><span>12 Elm Street</span><span>Springfield, ST</span></div><div class="web">www.brightpath.org</div></div>
  <div class="card card-front"><div class="sheen"></div><div class="org-line">BRIGHTPATH · PARTNER NETWORK</div><div class="name">Dana Whitfield</div><div class="title">Member</div><div class="rep-band"><span class="rep-label">REP</span><span class="rep-term">2013-2014</span></div><div class="contact"><span>555.010.2040</span><span>dana@brightpath.org</span><span>12 Elm Street</span><span>Springfield, ST</span></div><div class="web">www.brightpath.org</div></div>
  <div class="card card-front"><div class="sheen"></div><div class="org-line">BRIGHTPATH · PARTNER NETWORK</div><div class="name">Dana Whitfield</div><div class="title">Member</div><div class="rep-band"><span class="rep-label">REP</span><span class="rep-term">2013-2014</span></div><div class="contact"><span>555.010.2040</span><span>dana@brightpath.org</span><span>12 Elm Street</span><span>Springfield, ST</span></div><div class="web">www.brightpath.org</div></div>
  <div class="card card-front"><div class="sheen"></div><div class="org-line">BRIGHTPATH · PARTNER NETWORK</div><div class="name">Dana Whitfield</div><div class="title">Member</div><div class="rep-band"><span class="rep-label">REP</span><span class="rep-term">2013-2014</span></div><div class="contact"><span>555.010.2040</span><span>dana@brightpath.org</span><span>12 Elm Street</span><span>Springfield, ST</span></div><div class="web">www.brightpath.org</div></div>
  <div class="card card-front"><div class="sheen"></div><div class="org-line">BRIGHTPATH · PARTNER NETWORK</div><div class="name">Dana Whitfield</div><div class="title">Member</div><div class="rep-band"><span class="rep-label">REP</span><span class="rep-term">2013-2014</span></div><div class="contact"><span>555.010.2040</span><span>dana@brightpath.org</span><span>12 Elm Street</span><span>Springfield, ST</span></div><div class="web">www.brightpath.org</div></div>
</section>

</body>
</html>
```